Health Care Company with Logo Needs Business Cards designed

We are a luxury behavioral health company looking for business cards design we already have a logo and are looking for someone to design a sophisticated luxurious looking business card. Please note that Card design should be captivating just like the logo and also encompass the logo color

Industry/Entity Type

Healthcare

Contact Information for Business Card

Logo,company name, tagline, my name and title, contact details, and physical address

```html
<!DOCTYPE html>
<html lang="en">
<head>
<meta charset="utf-8">
<title>Orin Wellness Care – Business Card</title>
<link href="https://fonts.googleapis.com/css2?family=Roboto+Condensed:wght@700&family=Roboto:wght@400;500&family=Roboto+Mono:wght@700&display=swap" rel="stylesheet">
<style>
  :root {
    --stage: #2b2b2d;
    --blue-core: #0a93dc;
    --blue-mid: #1d78c8;
    --violet-edge: #6a55b0;
    --brand-purple: #6a2c8e;
    --brand-blue: #1a9ad9;
    --accent-orange: #e9a23b;
    --ink: #3a3a3a;
    --paper: #ffffff;
    --paper-shade: #ececee;
  }
  * { box-sizing: border-box; margin: 0; padding: 0; }
  html, body { width: 1200px; height: 900px; overflow: hidden; }
  body { background: var(--stage); position: relative; font-family: "Roboto", Arial, sans-serif; }

  .card {
    position: absolute;
    width: 620px;
    height: 354px;
    border-radius: 28px;
    overflow: hidden;
    box-shadow: 0 12px 30px rgba(0,0,0,0.45);
  }

  /* Front side */
  .card-front {
    left: 110px; top: 60px;
    background: radial-gradient(ellipse at 50% 45%, var(--blue-core) 0%, var(--blue-mid) 45%, var(--violet-edge) 100%);
    display: flex; align-items: center; justify-content: center;
  }
  .brand { display: flex; align-items: center; gap: 16px; }
  .brand-square { width: 46px; height: 46px; flex: none; }
  .card-front .brand-square { background: var(--paper); }
  .brand-name {
    font-family: "Roboto Condensed", "Arial Narrow", sans-serif;
    font-weight: 700; font-size: 44px; line-height: 1; letter-spacing: 0.5px;
  }
  .card-front .brand-name { color: var(--paper); }
  .brand-tagline {
    font-family: "Roboto Mono", monospace;
    font-weight: 700; font-size: 11.5px; letter-spacing: 2.4px;
    text-transform: uppercase; margin-top: 7px; white-space: nowrap;
  }
  .card-front .brand-tagline { color: var(--paper); }

  /* Back side */
  .card-back {
    left: 470px; top: 480px;
    background: linear-gradient(160deg, var(--paper) 0%, var(--paper-shade) 55%, var(--paper) 100%);
  }
  .card-back .brand { position: absolute; left: 40px; top: 40px; }
  .card-back .brand-square { background: var(--accent-orange); }
  .card-back .brand-name { color: var(--brand-purple); font-size: 38px; }
  .card-back .brand-tagline { color: var(--brand-blue); font-size: 10px; letter-spacing: 2.1px; }

  .person {
    position: absolute; right: 340px; top: 196px;
    text-align: right;
  }
  .person-title { color: var(--ink); font-size: 16px; }
  .person-name {
    font-family: "Roboto Condensed", "Arial Narrow", sans-serif;
    font-weight: 700; font-size: 24px; color: var(--brand-blue); margin-top: 2px;
  }
  .divider {
    position: absolute; left: 300px; top: 170px;
    width: 1.5px; height: 128px; background: var(--accent-orange);
  }
  .contact-list {
    position: absolute; left: 318px; top: 170px;
    list-style: none; color: var(--ink); font-size: 14.5px; line-height: 1.3;
  }
  .contact-list li { display: flex; align-items: flex-start; gap: 9px; margin-bottom: 6px; }
  .contact-list svg { width: 15px; height: 15px; flex: none; margin-top: 2px; fill: none; stroke: var(--brand-blue); stroke-width: 1.8; }
  .contact-list .filled { fill: var(--brand-blue); stroke: none; }
</style>
</head>
<body>
  <section class="card card-front" aria-label="Card front">
    <div class="brand">
      <span class="brand-square"></span>
      <div>
        <div class="brand-name">Orin Wellness Care</div>
        <div class="brand-tagline">Committed to calm, balance and renewal</div>
      </div>
    </div>
  </section>

  <section class="card card-back" aria-label="Card back">
    <div class="brand">
      <span class="brand-square"></span>
      <div>
        <div class="brand-name">Orin Wellness Care</div>
        <div class="brand-tagline">Committed to calm, balance and renewal</div>
      </div>
    </div>

    <div class="person">
      <div class="person-title">Director</div>
      <div class="person-name">DANA RIVERS</div>
    </div>

    <span class="divider"></span>

    <ul class="contact-list">
      <li>
        <svg viewBox="0 0 16 16"><rect x="4" y="1.5" width="8" height="13" rx="1.5"/><line x1="7" y1="12" x2="9" y2="12"/></svg>
        <span>0000 000 000</span>
      </li>
      <li>
        <svg viewBox="0 0 16 16"><rect x="1.5" y="3.5" width="13" height="9" rx="1"/><polyline points="1.5,4 8,9 14.5,4"/></svg>
        <span>dana@orinwellnesscare.com</span>
      </li>
      <li>
        <svg viewBox="0 0 16 16"><circle cx="8" cy="8" r="6.5"/><ellipse cx="8" cy="8" rx="3" ry="6.5"/><line x1="1.5" y1="8" x2="14.5" y2="8"/></svg>
        <span>www.orinwellnesscare.com</span>
      </li>
      <li>
        <svg viewBox="0 0 16 16"><path class="filled" d="M8 1a5 5 0 0 0-5 5c0 3.8 5 9 5 9s5-5.2 5-9a5 5 0 0 0-5-5zm0 7a2 2 0 1 1 0-4 2 2 0 0 1 0 4z"/></svg>
        <span>11 dummy city, dummy place<br>P.O Box 0000 Dummy Land</span>
      </li>
    </ul>
  </section>
</body>
</html>
```